Psychology service brochure

Marketing brochure for a new psychological counselling service.
Our old brochure was too boring and conservative. We are selling our services to GP's, psychiatrists, other health providers and of course potential clients. We'd really like a professional, elegant look that conveys us to be compassionate and conscientious providers of psychological services.
I have included a copy of our old brochure and a copy of the changes we'd like to the text.
Updates
I have included a photo of myself and my business partner. Only the faces are needed, so backgrounds would need to be edited out.
Hello, in consultation with my business partner, we would like
the use of our photos in the brochure please (with backgrounds edited out)
no stock photos of random people
use of abstract or nature/floral motifs suggestive of tranquillity
regards,
Miriam
Target Market(s)
General practitioner doctors, potential clients
Industry/Entity Type
Health
Requirements
Must have
- must include BlairMdITC TT- font for the business name
- must include our signature color Pantone 291 (see attached brochure)
- use of the photos of myself and my business partner (with background edited out please)
- keep use of colours to a minimum, 3 colors maximum, one of which must be Pantone 291
- must include changes to the brochure as outlined in the 'Changes to Pamphlet' document.
Nice to have
- an interesting, eye catching layout.
- interesting use of white spaces
- use of subtle abstract or nature/floral related graphics suggestive of tranquillity
Should not have
- should not include our fee
- stock photos of people

```html
<!DOCTYPE html>
<html lang="en">
<head>
<meta charset="utf-8">
<title>Stillwater Counselling – Brochure</title>
<link rel="stylesheet" href="https://fonts.googleapis.com/css2?family=Arimo:wght@400;700&family=Michroma&display=swap">
<style>
  :root {
    --aqua-pale: #aaf4fb;
    --aqua-text: #35d6e8;
    --aqua-soft: #c9f8fc;
    --aqua-line: #5ee3f0;
    --paper: #ffffff;
    --page: #ffffff;
  }
  * { box-sizing: border-box; margin: 0; padding: 0; }
  html, body { width: 1200px; height: 900px; overflow: hidden; background: var(--page); }
  body { position: relative; font-family: "Arimo", Arial, sans-serif; color: var(--aqua-text); }

  .brochure {
    position: absolute; left: 105px; top: 92px; width: 995px; height: 708px;
    background: var(--paper);
    box-shadow: 2px 4px 8px rgba(0,0,0,0.35);
    overflow: hidden;
  }
  .edge-strip { position: absolute; left: 0; top: 0; width: 20px; height: 100%; background: var(--aqua-pale); }

  .section-head {
    position: absolute; left: 20px; width: 249px; height: 54px;
    background: var(--aqua-pale);
    padding: 12px 0 0 36px;
    font-weight: 700; font-size: 15.5px; line-height: 20px; letter-spacing: 0.6px;
    color: var(--aqua-text); text-transform: uppercase; word-spacing: 3px;
  }
  .section-head::after {
    content: ""; position: absolute; left: 0; bottom: -4px; width: 309px; height: 4px;
    background: var(--aqua-pale);
  }
  .approach-head { top: 51px; }
  .clients-head { top: 345px; }

  .body-copy {
    position: absolute; left: 56px; width: 247px;
    font-size: 11.8px; line-height: 13.8px; letter-spacing: -0.1px;
    text-align: justify; hyphens: manual; color: var(--aqua-text);
  }
  .body-copy p + p { margin-top: 7px; }
  .approach-copy { top: 124px; }

  .client-goals { position: absolute; left: 56px; top: 416px; width: 247px; list-style: none; }
  .client-goals li {
    position: relative; padding-left: 13px; margin-bottom: 6.5px;
    font-size: 11.8px; line-height: 13.8px; letter-spacing: -0.1px; text-align: justify;
  }
  .client-goals li::before {
    content: ""; position: absolute; left: 1px; top: 5px; width: 4px; height: 4px;
    border-radius: 50%; background: var(--aqua-text);
  }

  .location-map {
    position: absolute; left: 356px; top: 110px; width: 274px; height: 276px;
    border: 1px solid var(--aqua-pale);
    background:
      linear-gradient(180deg, rgba(255,255,255,0) 0%, rgba(94,227,240,0.25) 50%, rgba(255,255,255,0) 100%),
      linear-gradient(90deg, #f4feff 0%, #bdf6fb 45%, #e3fcfe 60%, #bdf6fb 100%);
    box-shadow: 2px 3px 6px rgba(90,220,235,0.35);
  }

  .contact {
    position: absolute; left: 360px; top: 494px; width: 267px; text-align: center;
    font-size: 12.5px; line-height: 20.5px; font-style: normal;
  }
  .contact .centre-name { font-weight: 700; letter-spacing: 0.3px; }
  .contact-row { display: flex; justify-content: center; align-items: center; gap: 32px; font-weight: 700; }
  .contact-item { display: inline-flex; align-items: center; gap: 9px; }
  .contact-item svg { width: 20px; height: 18px; }

  .cover {
    position: absolute; left: 657px; top: 0; width: 338px; height: 100%; background: var(--aqua-pale);
  }
  .cover-title-band {
    position: absolute; left: 0; top: 45px; width: 100%; height: 33px; background: var(--paper);
    text-align: center; padding-top: 10px;
    font-family: "Michroma", sans-serif; font-size: 11px; font-variant: small-caps;
    letter-spacing: 1.2px; color: var(--aqua-text);
  }
  .cover-motif {
    position: absolute; left: 0; top: 100px; width: 270px; height: 608px;
    background:
      radial-gradient(ellipse 45% 30% at 45% 40%, rgba(255,255,255,0.45), rgba(255,255,255,0) 100%),
      radial-gradient(ellipse 40% 35% at 55% 75%, rgba(255,255,255,0.5), rgba(255,255,255,0) 100%),
      linear-gradient(180deg, rgba(255,255,255,0) 0%, rgba(255,255,255,0.25) 60%, rgba(255,255,255,0.15) 100%);
  }
  .cover-vertical-name {
    position: absolute; left: 276px; top: 652px; transform-origin: 0 0; transform: rotate(-90deg);
    white-space: nowrap; font-family: "Michroma", sans-serif; font-size: 21px; letter-spacing: 4.6px;
    line-height: 22px; color: rgba(255,255,255,0.85); text-transform: uppercase;
  }
</style>
</head>
<body>
  <main class="brochure">
    <div class="edge-strip"></div>

    <h2 class="section-head approach-head">Our approach<br>to therapy</h2>
    <div class="body-copy approach-copy">
      <p>We are warm, compassionate and pro&shy;fessional Clinical General Psychologists who together have thirty years of experience and who are committed to providing high quality evidence-based treatment to our clients.</p>
      <p>Types of treatment may include Cognitive Behavioural Therapy, Motivational Inter&shy;viewing and Mindfulness.</p>
    </div>

    <h2 class="section-head clients-head">What we want<br>for our clients</h2>
    <ul class="client-goals">
      <li>For you to feel heard and respected</li>
      <li>To have a positive experience of working collaboratively with a psychologist</li>
      <li>To connect or reconnect with feelings of hope</li>
      <li>To move beyond counselling with an understanding of your strengths and the skills to make changes that will help you to meet future challenges.</li>
    </ul>

    <div class="location-map" role="img" aria-label="Street map showing the centre on Linden Street, near Fairmont Station and the railway line"></div>

    <address class="contact">
      <div>Contact reception</div>
      <div class="centre-name">THE ASHBURY CENTRE</div>
      <div>18 Linden Street, Fairmont 3090</div>
      <div class="contact-row">
        <span class="contact-item">
          <svg viewBox="0 0 20 18" fill="none" stroke="#35d6e8" stroke-width="1.4"><path d="M2 6c0-2 3-3 8-3s8 1 8 3v1h-4V5.5H6V7H2z" fill="#35d6e8"/><rect x="4" y="9" width="12" height="7" rx="1.5"/><circle cx="10" cy="12.5" r="1.8"/></svg>
          9371 2604
        </span>
        <span class="contact-item">
          <svg viewBox="0 0 20 18" fill="none" stroke="#35d6e8" stroke-width="1.4"><rect x="5" y="1" width="9" height="6"/><rect x="2" y="7" width="16" height="9" rx="1"/><line x1="5" y1="11" x2="15" y2="11"/><line x1="5" y1="13.5" x2="15" y2="13.5"/></svg>
          9371 2605
        </span>
      </div>
      <div class="contact-row">
        <span class="contact-item">
          <svg viewBox="0 0 20 18" fill="none" stroke="#35d6e8" stroke-width="1.4"><rect x="1.5" y="3" width="17" height="12"/><path d="M1.5 3l8.5 7 8.5-7"/></svg>
          stillco@mailbox.com
        </span>
      </div>
    </address>

    <section class="cover">
      <div class="cover-title-band">Stillwater Counselling</div>
      <div class="cover-motif" role="img" aria-label="Delicate twining vine with leaves and spiral tendrils in pale aqua and white, rising the full height of the cover"></div>
      <div class="cover-vertical-name">Stillwater Counselling</div>
    </section>
  </main>
</body>
</html>
```